Header Design

I would like a new header design for my website - www.nestmarla.com.

I am a Realtor and the header should reflect that and complement the theme.

The attached logo needs to be included and the information that is already there. Also, the colors need to match.

Marla Quinby
Connecting you to the Los Angeles real estate scene.

Industry/Entity Type

Realtor

```html
<!DOCTYPE html>
<html lang="en">
<head>
<meta charset="utf-8">
<title>Marla Quinby – Los Angeles Real Estate</title>
<link href="https://fonts.googleapis.com/css2?family=Arimo:wght@400;700&display=swap" rel="stylesheet">
<style>
:root{
  --page:#444565;
  --plum:#3a2338;
  --plum-deep:#2f1c2d;
  --sky-top:#5a4c70;
  --sky-bottom:#3d3152;
  --panel:#ffffff;
  --shell:#e9e9ec;
  --line:#d8d8dc;
  --text:#444;
  --heading:#222;
  --blue:#2a7fe0;
  --orange:#e8782a;
}
*{box-sizing:border-box;margin:0;padding:0}
html,body{width:1200px;height:842px;overflow:hidden}
body{background:var(--page);font-family:"Arimo",Arial,sans-serif;color:var(--text);position:relative}
.site{position:absolute;left:81px;top:11px;width:1022px;height:840px;background:var(--shell);border:4px solid var(--plum-deep);border-bottom:none}
.masthead{position:absolute;left:0;top:0;width:1014px;height:128px;background:linear-gradient(180deg,var(--sky-top),var(--sky-bottom))}
.brand-mark{position:absolute;left:22px;top:22px;width:77px;height:79px;background:var(--plum-deep)}
.brand-name{position:absolute;left:117px;top:40px;color:#fff;font-size:30px;font-weight:400}
.brand-tagline{position:absolute;left:118px;top:81px;color:#fff;font-size:12.5px;letter-spacing:.3px;text-transform:uppercase}
.phone{position:absolute;right:0;top:0;width:159px;height:36px;background:var(--plum-deep);color:#fff;font-size:15.5px;display:flex;align-items:center;gap:12px;padding-left:16px}
.nav{position:absolute;left:0;top:128px;width:1014px;height:35px;background:var(--plum);display:flex;align-items:center;padding-left:17px}
.nav a{color:#fff;text-decoration:none;font-size:15px;margin-right:31px;white-space:nowrap}
.nav a:last-child{margin-right:0}
.main{position:absolute;left:10px;top:174px;width:644px;height:680px;background:var(--panel);border:1px solid #555}
.slider{position:absolute;left:15px;top:10px;width:613px;height:316px;background:linear-gradient(120deg,#d9dde0 0%,#c8ccd0 23%,#4e4a63 24%,#6d6a86 45%,#3a3238 70%,#c58a2c 90%,#d99a30 100%)}
.slider-arrow{position:absolute;top:140px}
.slider-label{position:absolute;left:7px;bottom:18px;background:#222;color:#fff;font-size:13.5px;padding:4px 8px}
.dots{position:absolute;left:248px;top:337px;display:flex;gap:11px}
.dots span{width:8px;height:8px;border-radius:50%;background:#bbb}
.dots span.on{background:#444}
.bar-title{background:var(--plum);color:#fff;font-size:11.5px;font-weight:700;text-transform:uppercase;padding:0 9px;height:23px;line-height:23px}
.news-title{position:absolute;left:5px;top:366px;width:623px}
.post{position:absolute;left:5px;width:623px}
.post-thumb{position:absolute;left:0;top:0;width:169px;height:169px;border:1px solid var(--line);padding:5px;background:#fff}
.post-thumb div{width:100%;height:100%;background:linear-gradient(180deg,#3f7fc7 0%,#8db3d8 55%,#a7a49a 80%,#6e6a60 100%)}
.post-body{position:absolute;left:179px;top:2px;width:444px}
.post h3{font-size:12.5px;color:var(--heading);font-weight:700;margin-bottom:6px}
.post p{font-size:12.5px;line-height:20px;color:#555;letter-spacing:-0.2px}
.post p a{background:var(--plum-deep);color:#fff;text-decoration:underline;padding:0 2px;white-space:nowrap}
.side-box{position:absolute;left:665px;width:340px;background:var(--panel);border:1px solid var(--line)}
.search{display:flex;margin:10px 0 0 10px}
.search span{width:245px;height:25px;border:1px solid #ccc;font-size:12px;line-height:23px;padding-left:6px;color:#444}
.search b{background:var(--plum-deep);color:#fff;font-size:11.5px;font-weight:700;height:25px;line-height:25px;padding:0 7px}
.rss{position:absolute;left:138px;top:9px;width:30px;height:30px;border-radius:5px;background:var(--orange)}
.share{position:absolute;right:10px;top:9px;width:28px;height:22px;border-radius:4px;background:#c34a3d}
.side-box .bar-title{margin:9px 10px 0}
.form-area{position:relative;padding-left:50px}
.form-area h4{font-size:17px;font-weight:700;color:var(--heading);border-bottom:1px solid #333;width:240px;padding-bottom:2px}
.field-label{font-size:10.5px;text-transform:uppercase;color:#444;margin:8px 0 6px}
.select{width:226px;height:27px;border:1px solid #aaa;font-size:12px;line-height:25px;padding-left:9px;position:relative}
.select::after{content:"";position:absolute;right:5px;top:5px;width:14px;height:15px;border:1px solid #999;border-radius:2px}
.price-row{display:flex;align-items:center;gap:6px;margin-top:31px;margin-left:4px}
.price-row .select{width:110px}
.submit{margin:22px 0 0 58px;width:180px;height:33px;background:var(--blue);border:1px solid #1a5db0;color:#fff;font-size:13px;text-align:center;line-height:31px}
.contact-row{display:flex;align-items:center;margin-top:10px}
.contact-row label{width:117px;text-align:right;font-size:12.5px;padding-right:8px;color:#444}
.contact-row span{width:161px;height:23px;border:1px solid #999}
.req{color:#d33;margin-left:3px;font-size:13px}
.post-divider{position:absolute;left:5px;top:575px;width:623px;border-top:1px solid var(--line)}
</style>
</head>
<body>
<div class="site">
  <header class="masthead" role="img" aria-label="Header banner with a purple-toned photograph of the downtown Los Angeles skyline">
    <div class="brand-mark"></div>
    <div class="brand-name">Marla Quinby</div>
    <div class="brand-tagline">Connecting you to the Los Angeles real estate scene</div>
    <div class="phone">
      <svg width="18" height="18" viewBox="0 0 24 24"><path fill="#fff" d="M6.6 10.8c1.4 2.8 3.8 5.1 6.6 6.6l2.2-2.2c.3-.3.7-.4 1-.2 1.1.4 2.3.6 3.6.6.6 0 1 .4 1 1V20c0 .6-.4 1-1 1C10.6 21 3 13.4 3 4c0-.6.4-1 1-1h3.5c.6 0 1 .4 1 1 0 1.3.2 2.5.6 3.6.1.3 0 .7-.2 1z"/></svg>
      310-555-0148
    </div>
  </header>
  <nav class="nav">
    <a>Home</a><a>About Marla</a><a>Home Search Central</a><a>Search By Community</a><a>Buyers</a><a>Sellers</a><a>Renters</a><a>Market Reports</a><a>Contact Me</a>
  </nav>

  <main class="main">
    <div class="slider" role="img" aria-label="Slideshow photograph of downtown Los Angeles towers at dusk with palm trees">
      <svg class="slider-arrow" style="left:18px" width="22" height="36" viewBox="0 0 22 36"><path d="M18 2 4 18l14 16" fill="none" stroke="#fff" stroke-opacity=".7" stroke-width="3"/></svg>
      <svg class="slider-arrow" style="right:18px" width="22" height="36" viewBox="0 0 22 36"><path d="M4 2l14 16L4 34" fill="none" stroke="#fff" stroke-opacity=".7" stroke-width="3"/></svg>
      <div class="slider-label">New Listings</div>
    </div>
    <div class="dots"><span></span><span></span><span></span><span></span><span class="on"></span><span></span><span></span></div>

    <div class="news-title bar-title">Los Angeles Real Estate News and Views</div>

    <article class="post" style="top:399px">
      <div class="post-thumb"><div role="img" aria-label="Photograph of Century City high-rise towers under a blue sky"></div></div>
      <div class="post-body">
        <h3>Century City Condos for Sale 2013 in Review</h3>
        <p>Century City condos have a mix of full service high rise buildings and gated garden complexes with full amenities.&nbsp; Away from the bustle and bustle with easy access to shopping and dining, Century City is a great alternative to the Wilshire Corridor. We should check in and see how the market performed in 2012 as compared with the previous year. Building Sold +/- 2011 Median +/- … <a>Continue Reading …</a></p>
      </div>
    </article>
    <div class="post-divider"></div>
    <article class="post" style="top:582px">
      <div class="post-thumb"><div role="img" aria-label="Photograph of the Westwood neighborhood skyline" style="background:linear-gradient(180deg,#b9cfe2,#d6e2ec)"></div></div>
      <div class="post-body">
        <h3>Westwood Homes for Sale 2013 in Review</h3>
        <p>Like most areas of Los Angeles, the Westwood neighborhood is suffering from low inventory, especially in the single family market. Home to Larkin College, it is</p>
      </div>
    </article>
  </main>

  <aside>
    <div class="side-box" style="top:175px;height:41px">
      <div class="search"><span>Search this website…</span><b>SEARCH</b></div>
    </div>
    <div class="side-box" style="top:226px;height:44px">
      <div class="rss"></div>
      <div class="share"></div>
    </div>
    <div class="side-box" style="top:283px;height:342px">
      <div class="bar-title">Find Your Next Home – Quick Search</div>
      <div class="form-area" style="margin-top:9px">
        <h4>Location</h4>
        <div class="field-label">City</div>
        <div class="select">Any</div>
        <div class="field-label" style="margin-top:12px">Community</div>
        <div class="select">Any</div>
        <h4 style="margin-top:18px">Property</h4>
        <div class="price-row"><div class="select">$0</div>-<div class="select">$0</div></div>
        <div class="submit">Search for Properties</div>
      </div>
    </div>
    <div class="side-box" style="top:637px;height:220px">
      <div class="bar-title">Need Help With Your Search?</div>
      <div class="contact-row" style="margin-top:10px"><label>Name</label><span></span><i class="req">*</i></div>
      <div class="contact-row" style="margin-top:8px"><label>Email</label><span></span><i class="req">*</i></div>
      <div class="contact-row" style="margin-top:8px"><label>Phone No.</label><span></span></div>
      <div class="contact-row" style="margin-top:8px;align-items:flex-start"><label style="margin-top:14px">How May I Help?</label><span style="width:192px;height:40px"></span><i class="req" style="margin-top:28px">*</i></div>
    </div>
  </aside>
</div>
</body>
</html>
```